Business Card Design Project

Small privately owned salon.

Industry/Entity Type

Business

Contact Information for Business Card

Hair salon.i would like my logo to be my name , Rosalind Marie. Address and phone can go on the front or back. The back will be where I write their appt.
address-527 Willowbend lane York, Pa. 17402
Phone- 717-464-3082

```html
<!DOCTYPE html>
<html lang="en">
<head>
<meta charset="utf-8">
<title>Rosalind Marie – Business Card</title>
<link href="https://fonts.googleapis.com/css2?family=Roboto:wght@400;700&display=swap" rel="stylesheet">
<style>
  :root {
    --bg: #fddcb5;
    --card-dark: #1e0c10;
    --accent: #ff7f00;
    --light: #ffffff;
    --ink: #2a1418;
  }
  * { box-sizing: border-box; margin: 0; padding: 0; }
  html, body { width: 1200px; height: 1200px; overflow: hidden; }
  body {
    background: var(--bg);
    font-family: 'Roboto', Arial, sans-serif;
    position: relative;
  }
  .card-front {
    position: absolute;
    left: 150px;
    top: 140px;
    width: 900px;
    height: 512px;
    background: var(--card-dark);
  }
  .ornament-band {
    position: absolute;
    left: 0;
    top: 10px;
    width: 900px;
    height: 76px;
  }
  .brand-name {
    position: absolute;
    left: 0;
    right: 0;
    top: 200px;
    text-align: center;
    font-size: 86px;
    font-weight: 400;
    color: var(--accent);
    letter-spacing: 1px;
  }
  .contact-line {
    position: absolute;
    left: 38px;
    right: 38px;
    top: 424px;
    display: flex;
    justify-content: space-between;
    font-size: 22px;
    letter-spacing: 1.6px;
    color: var(--light);
  }
  .accent { color: var(--accent); }
  .card-stripe {
    position: absolute;
    left: 0;
    top: 470px;
    width: 900px;
    height: 10px;
    background: var(--accent);
  }
  .card-back {
    position: absolute;
    left: 300px;
    top: 710px;
    width: 600px;
    height: 340px;
    background: var(--light);
    padding: 60px 48px 0;
  }
  .appointment-title {
    text-align: center;
    font-size: 16px;
    font-weight: 700;
    letter-spacing: 1px;
    color: var(--ink);
    margin-bottom: 30px;
  }
  .write-line {
    height: 1px;
    background: var(--ink);
    margin-bottom: 38px;
  }
</style>
</head>
<body>
  <section class="card-front">
    <svg class="ornament-band" viewBox="0 0 900 76" role="img" aria-label="Decorative orange and white flourish border">
      <rect x="0" y="0" width="900" height="76" fill="#ff7f00" opacity="0.55"/>
    </svg>
    <h1 class="brand-name">Rosalind Marie</h1>
    <div class="contact-line">
      <p class="address"><span class="accent">527</span> Willowbend lane York, <span class="accent">Pa.</span> 17402</p>
      <p class="phone">717-<span class="accent">464</span>-3082</p>
    </div>
    <div class="card-stripe"></div>
  </section>

  <section class="card-back">
    <h2 class="appointment-title">APPOINTMENT</h2>
    <div class="write-line"></div>
    <div class="write-line"></div>
    <div class="write-line"></div>
    <div class="write-line"></div>
    <div class="write-line"></div>
  </section>
</body>
</html>
```